OPF - Brochure 52 week Curriculum

Oak Path Fellows, Inc. wants to create a distribution Brochure. In the Bible (Matthew 28:18-20)- JESUS said to "TEACH" others what HE has commanded. we want to "PUT IN PRINT"

these 52 lines summarize HIS teachings
we want to use as our Curriculum teaching men ...

incorporate our statements and two main passages of scripture
(see attach pictures of headquarter lobby) to brand uniformity and consistency... we have summarized into 52 groups, but its NOT required to have numbers...
Purpose = obey GOD
Mission = love others
Vision = Development God fearing men globally.

The designer can have freedom in layout and sizing.
we were thinking bi fold , but again... designer has freedom
Please incorporate our colors (white, black, gray) using color wheel provided and our LOGO with website.

```html
<!DOCTYPE html>
<html lang="en">
<head>
<meta charset="UTF-8">
<title>Oak Path Fellows – Teach Brochure</title>
<link href="https://fonts.googleapis.com/css2?family=Poppins:wght@400;500;600;700;800&display=swap" rel="stylesheet">
<style>
  :root{
    --backdrop:#cbcbcb;
    --paper:#ffffff;
    --ink:#1a1a1a;
    --heading:#7d7d7f;
    --mid-gray:#8c8c8e;
    --light-gray:#a9a9a9;
    --dark:#0c0c0c;
    --num:#6f6f6f;
  }
  *{box-sizing:border-box;margin:0;padding:0}
  html,body{width:950px;height:1200px;overflow:hidden}
  body{background:var(--backdrop);font-family:"Poppins",sans-serif;color:var(--ink);position:relative}
  .spread{position:absolute;left:93px;width:764px;height:494px;display:flex}
  .spread--outside{top:82px}
  .spread--inside{top:623px}
  .panel{width:255px;height:494px;position:relative;overflow:hidden;background:var(--paper)}
  .panel--text{padding:20px 18px 0}
  .panel--fold{background:linear-gradient(90deg,#e6e6e6 0,#fafafa 14px,#fff 30px)}

  /* cover */
  .cover{background:linear-gradient(180deg,#8a8a8a 0%,#7a7a7a 45%,#3a3a3a 75%,#050505 100%)}
  .cover__art{position:absolute;left:20px;top:48px;width:215px;height:300px;border-radius:8px;
    background:radial-gradient(ellipse at 50% 45%,#9a9a9a 0%,#858585 55%,rgba(120,120,120,0) 80%)}
  .cover__ref{position:absolute;top:19px;left:0;width:100%;text-align:center;font-weight:700;font-size:11px;letter-spacing:7px;color:var(--light-gray)}
  .cover__lead{position:absolute;left:17px;top:362px;font-weight:700;font-size:29px;color:#fff;line-height:1}
  .cover__word{position:absolute;left:15px;top:392px;font-weight:800;font-size:62px;color:var(--mid-gray);line-height:1;letter-spacing:-1px;text-shadow:0 2px 4px rgba(0,0,0,.5)}
  .cover__pill{position:absolute;left:17px;top:455px;width:218px;height:22px;border-radius:11px;background:#0b0b0b;
    box-shadow:0 1px 3px rgba(255,255,255,.15);color:#fff;font-weight:600;font-size:10.5px;text-align:center;line-height:22px}

  h2{font-weight:700;font-size:11.5px;line-height:1.15;color:var(--heading);margin-bottom:6px}
  .list{list-style:none}
  .list li{position:relative;padding-left:8px;font-size:5.4px;line-height:6.8px;margin-bottom:6.6px;text-align:justify}
  .list li::before{content:attr(data-n);position:absolute;left:0;top:.3px;width:5px;height:5px;border-radius:50%;
    background:var(--num);color:#fff;font-size:2.8px;line-height:5px;text-align:center;font-weight:600}
  .section{margin-bottom:8px}

  .photo{border-radius:6px;width:219px;margin:2px 0 9px;position:relative}
  .photo--portrait{height:109px;background:linear-gradient(90deg,#141414 0%,#1e1e1e 55%,#4a4a4a 75%,#1a1a1a 100%)}
  .photo--portrait span{position:absolute;left:11px;top:8px;font-weight:700;font-size:10px;line-height:1.1;color:#a0a0a0}
  .photo--group{height:83px;background:linear-gradient(90deg,#3a3a3a,#8a8a8a 40%,#5a5a5a 70%,#2a2a2a)}
  .photo--cross{height:82px;background:radial-gradient(ellipse at 50% 70%,#f4f4f4,#c8c8c8 60%,#9a9a9a);margin-top:10px}
  .hands-art{position:absolute;right:6px;bottom:0;width:130px;height:92px;background:linear-gradient(180deg,rgba(60,60,60,.9),#1a1a1a);border-radius:6px 6px 0 0}

  .back-portrait{background:linear-gradient(160deg,#2a2a2a 0%,#3c3c3c 30%,#1a1a1a 60%,#0d0d0d 100%)}
  .back-portrait__art{position:absolute;inset:0}
  .back-portrait__ref{position:absolute;left:110px;top:265px;width:104px;text-align:center;font-weight:600;font-size:10.5px;letter-spacing:5px;line-height:13px;color:#bdbdbd}
</style>
</head>
<body>

<section class="spread spread--outside">
  <div class="panel cover">
    <div class="cover__art" role="img" aria-label="Faint painted portrait of a bearded apostle with raised open hands holding a cross"></div>
    <p class="cover__ref">MATTHEW 28:18-20</p>
    <p class="cover__lead">JESUS SAID TO</p>
    <p class="cover__word">TEACH</p>
    <p class="cover__pill">OTHERS WHAT HE HAS COMMANDED</p>
  </div>

  <div class="panel panel--text panel--fold">
    <div class="section">
      <h2>Regarding God<br>and Righteousness</h2>
      <ul class="list">
        <li data-n="1">Repent: Change your mind and actions towards sin, as the Kingdom of Heaven is near. Turn away from sin and toward GOD. Matthew 4:17, Luke 13:3. Repent: This is the call to turn away from sin and embrace the good news of salvation through Jesus Christ. Found in Mark 1:15.</li>
        <li data-n="2">Accept the Good News of salvation offered through Jesus.</li>
        <li data-n="3">Believe in the Son of God, Jesus Christ: This is essential for salvation and receiving the Holy Spirit. John 6:29, John 14:11</li>
        <li data-n="4">Have faith in God, and trust in Jesus as the Son of God.</li>
        <li data-n="5">Be born again: John 3:7 Be born again (of water and the Spirit): Experience a spiritual transformation necessary for entrance into God's Kingdom.</li>
        <li data-n="6">Give your utmost devotion and affection to God. Love God with all your heart, soul, mind, and strength: Matthew 22:37-38, Mark 12:30, Luke 10:27</li>
        <li data-n="7">Honor God's Law: Understand that Jesus did not come to abolish the Law but to fulfill it and to magnify its application in the heart.</li>
      </ul>
    </div>
    <div class="photo photo--portrait" role="img" aria-label="Painted portrait of a bearded apostle on a dark background"><span>MATTHEW<br>28:18-20</span></div>
    <div class="section">
      <h2>Regarding<br>Relationships and Ethics</h2>
      <ul class="list">
        <li data-n="8">Love your Neighbor as yourself: Matthew 22:39, Mark 12:31, Luke 10:27, Leviticus 19:18. Love one another, as I have loved you: Show sacrificial love to fellow believers.</li>
        <li data-n="9">The Golden Rule: Treat others as you would want to be treated. (Matthew 7:12). This encapsulates how to treat everyone with respect, kindness, and understanding.</li>
        <li data-n="10">Be reconciled to your brother: Seek peace and forgiveness when relationships are broken.</li>
        <li data-n="11">Go to those who offend you: Address offenses directly and privately before involving others.</li>
        <li data-n="12">Forgive offenders: Extend forgiveness to those who hurt you and forgive often. Forgive others: This is essential for receiving God's forgiveness.</li>
        <li data-n="13">Love your enemies and pray for those who persecute you: Matthew 5:44, Luke 6:27-28. Extend compassion even to those who mistreat you.</li>
      </ul>
    </div>
  </div>

  <div class="panel panel--text panel--fold">
    <div class="section">
      <h2>Regarding Personal<br>Conduct and Attitudes</h2>
      <ul class="list">
        <li data-n="14">Be baptized: Be immersed in water as a symbol of your new life in Christ.</li>
        <li data-n="15">Take, eat, and drink in remembrance of Me (Communion/Lord's Supper): Participate in the commemoration of Jesus' sacrifice.</li>
        <li data-n="16">Let your light shine before others: Matthew 5:16. Followers are called to live in such a way that their good deeds bring glory to GOD. Demonstrate good works to the world.</li>
        <li data-n="17">Care for the less fortunate: Help those in need, such as the hungry, thirsty, strangers, naked, sick, and imprisoned, according to Luke 14:13-14, Matthew 25:31-46.</li>
        <li data-n="18">Deny yourself, Take up your cross daily and follow Jesus: This signifies a commitment to discipleship, even in the face of hardship. this teaching is found in Luke 9:23-24; Matthew 16:24-25. Prioritize following Jesus above your own desires and be willing to endure hardship for His sake.</li>
        <li data-n="19">Fast: Engage in fasting, but do so for the right reasons and not for outward show.</li>
        <li data-n="20">Be wise as serpents and innocent as doves: Matthew 10:16</li>
        <li data-n="21">Do not worry about your life or material possessions: Trust God to provide for your needs. Trust God to provide for your needs. Matthew 6:34</li>
        <li data-n="22">Lay up treasures in heaven: Focus on building a spiritual inheritance rather than accumulating earthly wealth. Matthew 6:19-21</li>
        <li data-n="23">Be a servant: Seek greatness through humble service to others. Serve one another: Matthew 20:25-28</li>
      </ul>
    </div>
    <div class="section">
      <h2>Prayer</h2>
      <ul class="list">
        <li data-n="24">Jesus provided guidance on prayer, teaching that it should be done in private and with sincerity (Matthew 6:5-8).</li>
        <li data-n="25">He also linked prayer to having a forgiving heart (Mark 11:25; Matthew 18:18-20). HE encouraged praying with simple faith and persistence (Luke 11:5-13; Matthew 21:21-22).</li>
        <li data-n="26">Pray: Engage in prayer consistently, with sincerity and according to Jesus' example.</li>
        <li data-n="27">Prayer for our enemies : Luke 23:24, Matthew 5:44</li>
        <li data-n="28">Pray for others : intercession</li>
        <li data-n="29">Pray for laborers: Seek God to send workers into the harvest field of souls. Pray for kingdom laborers: Matthew 9:38, Luke 10:2</li>
      </ul>
    </div>
    <div class="hands-art" role="img" aria-label="Illustration of open hands raised beneath a cross, with faint crosses behind"></div>
  </div>
</section>

<section class="spread spread--inside">
  <div class="panel panel--text">
    <div class="section">
      <h2>Regarding Outreach<br>and Discipleship</h2>
      <ul class="list">
        <li data-n="30">Go and make disciples of all nations: Evangelize and teach others to follow Jesus' commands: This is a central command, emphasizing the importance of evangelism and discipleship. Matthew 28:18-20. Teach others to obey all that Jesus commanded: Passing on the teachings of Christ to new believers is a key aspect of discipleship.</li>
        <li data-n="31">Feed My Sheep: Care for and nourish the spiritual lives of believers.</li>
        <li data-n="32">Receive God's power: Be filled with the Holy Spirit to effectively carry out God's work.</li>
      </ul>
    </div>
    <div class="section">
      <h2>Cautions<br>and warnings</h2>
      <ul class="list">
        <li data-n="33">Beware of false prophets: Be discerning and recognize those who may mislead others with false teachings.</li>
        <li data-n="34">Beware of leaven (doctrine) of the Pharisees and Sadducees: Avoid hypocrisy and legalism.</li>
        <li data-n="35">Be alert and reliant on God's strength to overcome temptation.</li>
        <li data-n="36">Do not cast pearls before swine: Use discretion and avoid sharing sacred things with those who may devalue or disrespect them.</li>
      </ul>
    </div>
    <div class="photo photo--group" role="img" aria-label="Classical painting of a group of disciples gathered in discussion"></div>
    <div class="section">
      <h2>Living<br>as a Disciple</h2>
      <ul class="list">
        <li data-n="37">Be merciful: Show compassion to others, just as God is merciful. Act with kindness and compassion towards others. Luke 6:36</li>
        <li data-n="38">Care for those in distress: Help the hungry, thirsty, strangers, naked, sick, and imprisoned.</li>
        <li data-n="39">Recognize your own imperfections and avoid judging others harshly. Matthew 7:1-2, Luke 6:37. Focus on examining your own faults before criticizing others. He taught against judging others, stating that the standard by which you judge will be applied to you (Matthew 7:1-2).</li>
        <li data-n="40">Seek God's kingdom first: Make God and his righteousness your highest priority. Prioritize God's reign and right way of living above all else. Found in Matthew 6:33.</li>
        <li data-n="41">Abide in JESUS: John 15:4, John 6:35, 40, 47, John 14:27.</li>
        <li data-n="42">Follow JESUS: Matthew 4:19, Luke 5:28</li>
      </ul>
    </div>
  </div>

  <div class="panel panel--text panel--fold">
    <div class="section" style="margin-bottom:20px">
      <h2>Forgiveness (Jesus Taught About The Importance Of Both Receiving and Giving Forgiveness)</h2>
      <ul class="list">
        <li data-n="43">Forgive others: Matthew 6:12, 14, Mark 11:25-26, Luke 6:37</li>
        <li data-n="44">JESUS emphasized that forgiveness is linked to forgiving others (Matthew 6:14-15)</li>
        <li data-n="45">forgiveness should be extended limitlessly to those who repent (Luke 17:3-4; Matthew 18:21-22).</li>
        <li data-n="46">forgiveness is also illustrated as the cancellation of debt (Matthew 18:21-35).</li>
      </ul>
    </div>
    <div class="section" style="margin-bottom:20px">
      <h2>Humility and Service</h2>
      <ul class="list">
        <li data-n="47">JESUS stated that humility leads to being honored (Luke 14:11; Matthew 23:12)</li>
        <li data-n="48">True greatness is found in serving others (Matthew 20:26-28).</li>
        <li data-n="49">The Bible also states that God opposes the proud but shows favor to the humble (James 4:6; 1 Peter 5:5).</li>
      </ul>
    </div>
    <div class="section" style="margin-bottom:20px">
      <h2>Warning Against Self<br>Righteousness and Judgment</h2>
      <ul class="list">
        <li data-n="50">Jesus warned against hypocrisy, particularly the hypocrisy of the Pharisees (Luke 12:1).</li>
      </ul>
    </div>
    <div class="section">
      <h2>Money (Jesus Taught About Using Money and Possessions Responsibly.</h2>
      <ul class="list">
        <li data-n="51">JESUS advised storing up treasures in Heaven rather than on Earth (Matthew 6:19-21)</li>
        <li data-n="52">JESUS stated that it is impossible to serve both God and money (Matthew 6:24).</li>
      </ul>
    </div>
    <div class="photo photo--cross" role="img" aria-label="Silhouette of a crucifix against a bright cloudy sky"></div>
  </div>

  <div class="panel back-portrait">
    <div class="back-portrait__art" role="img" aria-label="Painted portrait of a bearded apostle holding a book, on a dark background"></div>
    <p class="back-portrait__ref">MATTHEW<br>28:18-20</p>
  </div>
</section>

</body>
</html>
```